"MEET THE TEAM" page web design

We need a "meet the team" page for our website!
Please look at our website to see the style we need

We are looking for something unique, fun, cool, technology-style and yet professional. We plan on taking a picture of each employee (not sure if this will be a real photo/caricature/ black and white/goofy picture--> but we are open to any ideas you have that will work with the design) and putting it there, along with a little bio about each person.

Thanks! looking forward to working together:)
Updates

Project Deadline Extended
Reason: I am excited to see more designs and find the perfect fit. Thanks designers :)

Target Market(s)

People looking to purchase servers, workstations, components

Industry/Entity Type

Information Technology

Number of Pages Required

1 page

Font styles to use
Sans Serif
Other font styles liked:
• The font we use on our site so it matches

Requirements
Must have
• please look at our website quenditrex.com and see the theme and colors we want.
• We have 13 employees but would like to have a design where we can add/remove people if we hire/terminate them without messing up the design.
• We are looking for something unique, fun, cool, technology-style and yet professional. We plan on taking a picture of each employee (not sure if this will be a real photo/caricature/ black and white/goofy picture--> but we are open to any ideas you have that will work with the design) and putting it there, along with a little bio about each person.
• We can upload anything you need
Nice to have
• We are also interested in having a design where when the cursor moves over a person then the bio comes out or moves around, or something. (This is not required, but we would love some cool ideas) And if you can come up with some design, we would have our programmers create it for us.
Should not have
• we are open to anything

```html
<!DOCTYPE html>
<html lang="en">
<head>
<meta charset="utf-8">
<title>Meet the Team – Quenditrex</title>
<link href="https://fonts.googleapis.com/css2?family=Open+Sans:wght@400;600&family=Arimo:wght@400&display=swap" rel="stylesheet">
<style>
  :root{
    --teal:#2aa9a0;
    --teal-dark:#1d8d85;
    --teal-line:#35d1bd;
    --forest:#124a40;
    --ink:#333;
    --muted:#a9a9a9;
    --footer:#a6a6a6;
    --footer-dark:#9a9a9a;
    --white:#fff;
  }
  *{box-sizing:border-box;margin:0;padding:0}
  html,body{width:750px;height:1200px;overflow:hidden;background:var(--white)}
  body{position:relative;font-family:'Open Sans',sans-serif;color:var(--ink)}
  .abs{position:absolute}

  /* header */
  .site-header{position:absolute;left:0;top:0;width:750px;height:63px;border-bottom:1px solid #e6e6e6}
  .brand{left:40px;top:18px;display:flex;align-items:center;gap:10px}
  .brand-mark{width:30px;height:30px;border-radius:50%;background:var(--teal)}
  .brand-name{font-size:22px;font-weight:400;color:var(--teal);letter-spacing:2px}
  .account-tab{left:592px;top:0;width:120px;height:21px;background:#9b9b9b;border-radius:0 0 14px 14px;display:flex;font-size:7px;color:#eee;align-items:center}
  .account-tab span{flex:1;text-align:center}
  .account-tab span+span{border-left:1px solid #bbb}
  .contact-chip{top:30px;display:flex;align-items:center;gap:8px;font-size:9px;color:#555}
  .contact-chip .icon{width:26px;height:26px;border:1px solid #ddd;border-radius:50%;display:flex;align-items:center;justify-content:center}
  .phone-number{font-size:12px;color:#333}

  .main-nav{left:0;top:63px;width:750px;height:31px}
  .main-nav ul{list-style:none;position:absolute;left:39px;top:11px;display:flex;gap:16px;font-size:7px;color:#444;letter-spacing:.2px}
  .search{left:582px;top:69px;width:124px;height:22px;border:1px solid #ccc;border-radius:11px;font-size:7px;padding:7px 13px;color:#555}
  .search svg{position:absolute;right:8px;top:5px}
  .cart{left:691px;top:67px;width:25px;height:25px;border:1px solid #ccc;border-radius:50%;display:flex;align-items:center;justify-content:center}

  /* title band */
  .title-band{left:0;top:94px;width:750px;height:59px;background:var(--teal)}
  .title-band h1{position:absolute;left:38px;top:20px;font-size:15px;font-weight:400;color:var(--white)}
  .breadcrumb{position:absolute;left:598px;top:20px;width:116px;height:22px;background:var(--teal-dark);color:var(--white);font-size:9px;text-align:center;line-height:22px}

  /* team grid */
  .member{position:absolute;width:210px}
  .member .photo{height:196px}
  .member .info{height:110px;border:2px solid var(--teal-line);border-top:none;text-align:center;background:var(--white)}
  .member h2{font-size:12px;font-weight:400;color:var(--teal);padding-top:30px}
  .member .rule{width:66px;margin:11px auto 0;border-top:1px solid #ccc;height:4px;border-bottom:1px solid #ccc}
  .member .role{font-size:10px;color:var(--muted);margin-top:13px}

  .featured{position:absolute;left:43px;top:178px;width:210px;height:306px;background:var(--forest);color:var(--white);padding:26px 18px 0 20px}
  .featured p{font-size:10.5px;line-height:16.7px}
  .featured h2{font-size:12px;font-weight:400;color:var(--teal-line);margin-top:18px}
  .featured .role{font-size:10px;color:#b9c9c5;margin-top:4px}
  .featured .socials{display:flex;gap:9px;margin-top:22px}
  .featured .socials span{width:10px;height:10px;border-radius:50%;border:1.5px solid var(--teal-line)}

  .pager{left:334px;top:845px;display:flex;align-items:center;gap:10px;font-size:9px;color:#555}
  .pager .current{width:18px;height:18px;border:1px solid #ccc;text-align:center;line-height:16px;color:#aaa;font-size:7px}
  .pager b{font-weight:600}

  /* footer */
  .site-footer{left:0;top:893px;width:750px;height:307px;background:var(--footer);font-family:'Arimo',sans-serif;color:var(--white)}
  .about{position:absolute;left:230px;top:10px;width:330px;text-align:center;font-size:9px;line-height:12.3px}
  .contacts{position:absolute;left:228px;top:92px;display:flex;gap:18px;font-size:9px;line-height:12px}
  .contacts div{display:flex;gap:6px}
  .footer-cols{position:absolute;left:206px;top:133px;display:flex;gap:0;font-size:10px}
  .footer-cols > div{width:85px}
  .footer-cols .support{width:110px;text-align:center}
  .footer-cols small{display:block;font-size:6px;line-height:8.8px;margin-top:3px}
  .footer-base{position:absolute;left:0;top:195px;width:750px;height:112px;background:var(--footer-dark)}
  .social-row{position:absolute;left:307px;top:13px;display:flex;gap:11px}
  .social-row span{width:23px;height:23px;border:1px solid #ccc;border-radius:50%}
  .base-rule{position:absolute;left:110px;top:52px;width:530px;border-top:1px solid #b5b5b5}
  .legal{position:absolute;left:343px;top:61px;display:flex;gap:6px;align-items:center;font-size:8px;line-height:11px}
  .legal .dot{width:14px;height:14px;border-radius:50%;background:#ddd}
  .chat-now{left:608px;top:1184px;width:133px;height:16px;background:var(--teal);color:var(--white);font-size:8px;font-weight:600;padding:3px 6px;border-radius:2px 2px 0 0}
</style>
</head>
<body>

<header class="site-header">
  <div class="abs brand"><span class="brand-mark"></span><span class="brand-name">QUENDITREX</span></div>
  <div class="abs account-tab"><span>SIGN UP</span><span>LOGIN</span></div>
  <div class="abs contact-chip" style="left:522px">
    <span class="icon"><svg width="11" height="10" viewBox="0 0 11 10"><path d="M1 1h9v6H5l-3 2V7H1z" fill="#2aa9a0"/></svg></span>LIVE CHAT
  </div>
  <div class="abs contact-chip" style="left:608px">
    <span class="icon"><svg width="10" height="10" viewBox="0 0 10 10"><path d="M2 1l2 2-1 1c1 1.5 2 2.5 3 3l1-1 2 2-1.5 1.5C4 9 1 6 .5 2.5z" fill="#2aa9a0"/></svg></span><span class="phone-number">555-014-2290</span>
  </div>
</header>

<nav class="abs main-nav">
  <ul>
    <li>SERVERS</li><li>WORKSTATIONS</li><li>COMPONENTS</li><li>VIRTUAL REALITY</li><li>DRONES</li><li>ABOUT US</li><li>BLOG</li><li>RESOURCES</li><li>CONTACT US</li>
  </ul>
</nav>
<div class="abs search">Search<svg width="10" height="10" viewBox="0 0 10 10"><circle cx="4" cy="4" r="3" fill="none" stroke="#2aa9a0" stroke-width="1.5"/><path d="M6 6l3 3" stroke="#2aa9a0" stroke-width="1.5"/></svg></div>
<div class="abs cart"><svg width="12" height="10" viewBox="0 0 12 10"><path d="M1 2h10l-1 6H2z" fill="none" stroke="#2aa9a0" stroke-width="1.4"/></svg></div>

<section class="abs title-band">
  <h1>MEET THE TEAM</h1>
  <div class="breadcrumb">Homepage / our team</div>
</section>

<article class="featured">
  <p>Lorem ipsum dolor sit amet, sectetur adipiscing elit. Donec id magna nec urna dictum interdum. Praesent in mauris ac nulla sodales dignissim tincidunt quis lacus. Curabitur interdum sed ante in tempor. Nunc id ligula sed erat pellentesque hendrerit. Etiam felis tellus, euismod nec elit at, faucibus malesuada ipsum.</p>
  <h2>Nick Anderson</h2>
  <div class="role">Expert Agent</div>
  <div class="socials"><span></span><span></span><span></span><span></span><span></span><span></span></div>
</article>

<article class="member" style="left:270px;top:178px">
  <div class="photo" role="img" aria-label="Portrait of Jonathan Doe in a suit in an office" style="background:linear-gradient(160deg,#c9cfd3,#6f6a66 60%,#2c3040)"></div>
  <div class="info"><h2>Jonathan Doe</h2><div class="rule"></div><div class="role">expert agent</div></div>
</article>
<article class="member" style="left:498px;top:178px">
  <div class="photo" role="img" aria-label="Portrait of Alexandra in a white jacket" style="background:linear-gradient(160deg,#e4e4e2,#b79a86 55%,#efeeec)"></div>
  <div class="info"><h2>Alexandra</h2><div class="rule"></div><div class="role">expert agent</div></div>
</article>
<article class="member" style="left:43px;top:510px">
  <div class="photo" role="img" aria-label="Portrait of John Smith in a suit and red tie against the sky" style="background:linear-gradient(170deg,#7fa5d6,#b9cde6 50%,#2a2d35)"></div>
  <div class="info"><h2>John Smith</h2><div class="rule"></div><div class="role">expert agent</div></div>
</article>
<article class="member" style="left:270px;top:510px">
  <div class="photo" role="img" aria-label="Portrait of Marek Velinsky in a checked shirt" style="background:linear-gradient(170deg,#dadcdc,#b08a72 45%,#3f4f67)"></div>
  <div class="info"><h2>Marek Velinsky</h2><div class="rule"></div><div class="role">expert agent</div></div>
</article>
<article class="member" style="left:498px;top:510px">
  <div class="photo" role="img" aria-label="Portrait of Nick Anderson on the phone outdoors" style="background:linear-gradient(170deg,#8f9a88,#c7a992 45%,#2b2d33)"></div>
  <div class="info"><h2>Nick Anderson</h2><div class="rule"></div><div class="role">expert agent</div></div>
</article>

<nav class="abs pager"><span class="current">1</span><b>2</b><b>next ›</b></nav>

<footer class="abs site-footer">
  <p class="about">Based in Fenwick Park California, Quenditrex offers custom servers, storage, and workstations for local businesses in Los Angeles, Beverly Hills, Thousand Oaks, Ventura, Orange County, Santa Barbara, Oxnard, Irvine, Anaheim, and San Diego. Quenditrex also offers such products to clients throughout the United States and Worldwide.</p>
  <div class="contacts">
    <div><svg width="8" height="10" viewBox="0 0 8 10"><path d="M4 10C1 6 0 4.5 0 4a4 4 0 018 0c0 .5-1 2-4 6z" fill="#fff"/><circle cx="4" cy="4" r="1.4" fill="#a6a6a6"/></svg><span>4820 Larkmoor Ave.<br>Fenwick Park, CA 90210</span></div>
    <div><svg width="9" height="9" viewBox="0 0 10 10"><path d="M2 1l2 2-1 1c1 1.5 2 2.5 3 3l1-1 2 2-1.5 1.5C4 9 1 6 .5 2.5z" fill="#fff"/></svg><span>555-014-2290</span></div>
    <div><svg width="10" height="8" viewBox="0 0 10 8"><rect width="10" height="8" fill="#fff"/><path d="M0 0l5 4 5-4" fill="none" stroke="#a6a6a6"/></svg><span>sales@quenditrex.com</span></div>
  </div>
  <div class="footer-cols">
    <div>Hardware</div><div style="padding-left:20px">Drones</div><div>Mobility</div><div style="padding-left:10px">About</div>
    <div class="support">Customer Support<small>Terms and<br>Conditions<br>Warranty Information<br>Contact Us<br>Return Policy</small></div>
  </div>
  <div class="footer-base">
    <div class="social-row"><span></span><span></span><span></span><span></span></div>
    <div class="base-rule"></div>
    <div class="legal"><span class="dot"></span><span>Quenditrex, LLC.<br>Copyright © 2017</span></div>
  </div>
</footer>

<div class="abs chat-now">CHAT NOW<svg style="position:absolute;right:6px;top:4px" width="9" height="6" viewBox="0 0 9 6"><path d="M1 5l3.5-3.5L8 5" fill="none" stroke="#fff" stroke-width="1.4"/></svg></div>

</body>
</html>
```